Investment company needing business card

We are wanting a business card which looks sharp and easy on the eye. We are thinking of having a business card with the logo embossed on it, to really make it stand out. We will only have a small amount of information of the business card, person's name, position, email address and phone number

Contact Information for Business Card

Danica Pruett
Executive Assistant
+64 21 547 3162
danicap@harwellcapital.co.nz

Requirements
Must have
• Embossed logo
Should not have
• Not to be busy

```html
<!DOCTYPE html>
<html lang="en">
<head>
<meta charset="UTF-8">
<title>Harwell Capital — Business Card</title>
<link rel="stylesheet" href="https://fonts.googleapis.com/css2?family=Montserrat:wght@500;600&family=Raleway:wght@300;400&display=swap">
<style>
  :root {
    --backdrop: #efefef;
    --card-green: #14b33c;
    --text-white: #ffffff;
    --text-soft: #e4f7e8;
    --mark-grey: #4b5350;
  }
  * { box-sizing: border-box; margin: 0; padding: 0; }
  html, body {
    width: 1200px;
    height: 900px;
    overflow: hidden;
    background: var(--backdrop);
  }
  .canvas {
    position: relative;
    width: 1200px;
    height: 900px;
  }
  .business-card {
    position: absolute;
    left: 110px;
    top: 170px;
    width: 980px;
    height: 560px;
    background: var(--card-green);
    border-radius: 4px;
  }
  .brand {
    position: absolute;
    left: 90px;
    top: 300px;
    display: flex;
    align-items: center;
    gap: 18px;
  }
  .brand-square {
    width: 58px;
    height: 58px;
    background: var(--mark-grey);
  }
  .brand-name {
    font-family: "Montserrat", sans-serif;
    font-weight: 600;
    font-size: 40px;
    letter-spacing: 3px;
    text-transform: uppercase;
    color: var(--mark-grey);
  }
  .contact {
    position: absolute;
    right: 70px;
    top: 110px;
    text-align: right;
    color: var(--text-white);
  }
  .person-name {
    font-family: "Montserrat", sans-serif;
    font-weight: 500;
    font-size: 34px;
    line-height: 1.1;
  }
  .person-role {
    font-family: "Raleway", sans-serif;
    font-weight: 400;
    font-size: 17px;
    letter-spacing: 1px;
    text-transform: uppercase;
    margin-top: 4px;
  }
  .contact-list {
    list-style: none;
    margin-top: 46px;
  }
  .contact-item {
    display: flex;
    justify-content: flex-end;
    align-items: center;
    gap: 14px;
    font-family: "Raleway", sans-serif;
    font-weight: 300;
    font-size: 16px;
    letter-spacing: 0.5px;
    color: var(--text-soft);
    margin-bottom: 22px;
  }
  .contact-icon {
    width: 18px;
    height: 18px;
    fill: var(--text-white);
    flex: none;
  }
</style>
</head>
<body>
<main class="canvas">
  <section class="business-card">
    <div class="brand">
      <span class="brand-square"></span>
      <span class="brand-name">Harwell Capital</span>
    </div>
    <div class="contact">
      <h1 class="person-name">Danica Pruett</h1>
      <p class="person-role">Executive Assistant</p>
      <ul class="contact-list">
        <li class="contact-item">
          <span>+64 21 547 3162</span>
          <svg class="contact-icon" viewBox="0 0 24 24" aria-hidden="true">
            <path d="M6.6 10.8a15.1 15.1 0 0 0 6.6 6.6l2.2-2.2c.3-.3.7-.4 1-.2 1.1.4 2.3.6 3.6.6.6 0 1 .4 1 1V20c0 .6-.4 1-1 1A17 17 0 0 1 3 4c0-.6.4-1 1-1h3.5c.6 0 1 .4 1 1 0 1.3.2 2.5.6 3.6.1.3 0 .7-.2 1z"/>
          </svg>
        </li>
        <li class="contact-item">
          <span>danicap@harwellcapital.co.nz</span>
          <svg class="contact-icon" viewBox="0 0 24 24" aria-hidden="true">
            <path d="M2 5h20v14H2z M3.5 6.5v.4l8.5 6 8.5-6v-.4z" fill-rule="evenodd"/>
          </svg>
        </li>
      </ul>
    </div>
  </section>
</main>
</body>
</html>
```